lantern pathway for children needs a website designer

We need a website designer for our new extension to our company known as 'lantern pathway' providing shadow support services to children based in Singapore. We are a sister branch of a private clinic 'Bright horizon' providing speech language, occupational, and educational therapy to children.

We would like to use our own photos. So the selected design should have a frame with pictures to give us an idea but we will replace them with our own. We will be needing help with inputting information and changing information throughout.

We would like to see designs that are simple, and professional. We have a logo (see attached). The result should convey professionalism in shadow support, fostering independent thinking and moving students towards self-learning.

Target Market(s)

Teachers, psychologists, parents

Industry/Entity Type

Clinic

Requirements
Should not have
• too distracting colours

```html
<!DOCTYPE html>
<html lang="en">
<head>
<meta charset="utf-8">
<title>Lantern Pathway</title>
<link href="https://fonts.googleapis.com/css2?family=Cabin:wght@400;600&family=Lato:ital,wght@0,300;0,400;1,300&family=Arimo&display=swap" rel="stylesheet">
<style>
:root{
  --brand:#8a0b0b;
  --brand-dark:#6e0606;
  --ink:#333;
  --muted:#555;
  --panel:#f1f1f1;
  --line:#d6d6d6;
  --button:#6b6b6b;
  --footer:#0d0d0d;
}
*{margin:0;padding:0;box-sizing:border-box}
html,body{width:904px;height:1200px;overflow:hidden;background:#fff}
.page{position:relative;width:904px;height:1200px;font-family:'Lato',sans-serif;color:var(--ink)}
.abs{position:absolute}
.topbar{left:0;top:0;width:904px;height:4px;background:var(--brand)}
.brand{left:65px;top:44px;font-family:'Cabin',sans-serif;font-weight:600;font-size:27px;color:var(--brand);display:flex;align-items:center;gap:8px}
.brand-mark{width:14px;height:14px;border-radius:50%;background:var(--brand)}
.nav{top:56px;left:400px;display:flex;font-family:'Arimo',sans-serif;font-size:13px;color:#222}
.nav a{color:inherit;text-decoration:none;height:24px;line-height:24px}
.nav .active{background:var(--brand);color:#fff;padding:0 9px;width:51px;text-align:center}
.hero{left:0;top:107px;width:904px;height:404px;background:linear-gradient(100deg,#e4e4e2 0%,#f3f3f1 40%,#ecebe8 65%,#d9d4cf 100%)}
.caption{left:67px;top:377px;width:512px;height:108px;background:rgba(110,110,110,.78);color:#fff;padding:16px 29px}
.caption h1{font-family:'Cabin',sans-serif;font-weight:600;font-size:28px;line-height:1.2}
.caption p{font-weight:300;font-size:22px;margin-top:6px}
.dots{left:801px;top:485px;display:flex;gap:3px}
.dots i{width:6px;height:6px;border-radius:50%;background:#222;display:block}
.dots i:first-child{background:#fff;border:1px solid #222}
.h2{font-family:'Cabin',sans-serif;font-size:18px;color:var(--brand);font-weight:400}
.welcome-copy{left:65px;top:581px;width:445px;font-size:11px;line-height:19px;color:var(--muted);font-weight:300}
.welcome-copy p{margin-bottom:2px}
.service{width:198px}
.service .photo{width:198px;height:114px}
.service h3{font-family:'Cabin',sans-serif;font-weight:400;font-size:14px;color:#444;margin:20px 0 8px}
.service p{font-size:11px;line-height:19px;color:var(--muted);font-weight:300}
.more{display:block;margin:15px 0 0 auto;width:81px;height:26px;background:var(--button);color:#fff;font-family:'Cabin',sans-serif;font-size:12px;text-align:center;line-height:26px}
.register{left:586px;top:551px;width:253px;height:285px;background:var(--panel);border:1px solid #e2e2e2}
.register header{height:38px;background:linear-gradient(#a01313,var(--brand-dark));color:#fff;font-family:'Cabin',sans-serif;font-weight:600;font-size:17px;line-height:38px;padding-left:14px}
.register .intro{font-size:11px;line-height:19px;color:var(--muted);padding:12px 12px 0;font-weight:300}
.field{display:block;width:229px;height:33px;margin:11px 0 0 12px;background:#fff;border:1px solid var(--line);font-size:11px;color:#666;padding:0 12px;line-height:31px;font-weight:300}
.field:first-of-type{margin-top:14px}
.signup{position:absolute;right:12px;top:244px;width:61px;height:27px;background:linear-gradient(#555,#2c2c2c);color:#fff;border-radius:2px;font-family:'Cabin',sans-serif;font-size:13px;text-align:center;line-height:27px}
.arrows{left:802px;top:874px;display:flex;gap:3px}
.quote{left:603px;top:925px;width:232px;font-style:italic;font-size:10px;line-height:18px;color:#444;font-weight:300}
.qmark{color:#bbb;font-size:18px;font-family:Georgia,serif}
.author{left:752px;top:1051px;font-size:10px;font-weight:400;color:#222;display:flex;align-items:center;gap:8px}
.footer{left:0;top:1121px;width:904px;height:79px;background:var(--footer);color:#fff;font-family:'Arimo',sans-serif;font-size:11px}
.footer .links{position:absolute;left:65px;top:20px}
.footer .copy{position:absolute;left:65px;top:46px}
.social{position:absolute;top:25px;left:701px;display:flex;gap:10px}
.social i{display:block;width:27px;height:27px}
</style>
</head>
<body>
<div class="page">
  <div class="abs topbar"></div>
  <div class="abs brand"><span class="brand-mark"></span>Lantern Pathway</div>
  <nav class="abs nav">
    <a class="active" href="#">About</a>
    <a href="#" style="margin-left:19px">Mission</a>
    <a href="#" style="margin-left:28px">Our Services</a>
    <a href="#" style="margin-left:28px">Shadow Support</a>
    <a href="#" style="margin-left:28px">For Referrers</a>
  </nav>

  <div class="abs hero" role="img" aria-label="Photo of a therapist in a white coat smiling beside a young boy working at a table"></div>
  <div class="abs caption">
    <h1>Typinon habent claritatem processus</h1>
    <p>Duis autem vel eum iriure dolor claritas est</p>
  </div>
  <div class="abs dots"><i></i><i></i><i></i><i></i></div>

  <h2 class="abs h2" style="left:67px;top:546px">Welcome to Our Website!</h2>
  <div class="abs welcome-copy">
    <p>Naserndе orodiaer leroase custium reuentis kertyades vetati etchitecto beataemose keriase rtas tores!</p>
    <p>Lasodiaer leroas accusa ntium reue kentiulose riasertas Inventore veritati etchitecto beatae vitae dicta sunt, explicabo. Nemo enim ipsam volu temquia voluptas sispernatur aut oditau t fugited quia consequr magni dolores eosert, qui ratione voluptatem sequi nesciunt.</p>
    <p>Lasodiaer leroas accntium reuekentie riasesa Inveveritati etchcto beatae vitae dictuntaxplic versa. Nemo ispernadit aut fugitedoases uiratsequse nesciunt masrtades basetase.</p>
    <p>Duis autem vel eum iriure dolor in hendrerit in vulputate velit esse molestie consequat.</p>
  </div>

  <h2 class="abs h2" style="left:66px;top:790px">Our Services</h2>
  <div class="abs service" style="left:66px;top:829px">
    <div class="photo" role="img" aria-label="Photo of a therapist playing with a toddler among colourful toys" style="background:linear-gradient(90deg,#cfd9e4,#eae3cf,#9fb7c9)"></div>
    <h3>TRAIN SHADOWS</h3>
    <p>Lasodiaer leroas accntium reuekentie rias esa Inveveritati etchcto beatae vitae dicti untaxplic versa. Nemo ispernadit aut.</p>
    <span class="more">READ MORE</span>
  </div>
  <div class="abs service" style="left:307px;top:829px">
    <div class="photo" role="img" aria-label="Photo of a teacher reading with a young girl in a playroom" style="background:linear-gradient(90deg,#c9b9a3,#6d5a4d,#3b4f74)"></div>
    <h3>REFERRERS</h3>
    <p>Lasodiaer leroas accntium reuekentie rias esa Inveveritati etchcto beatae vitae dicti untaxplic versa. Nemo ispernadit aut.</p>
    <span class="more">READ MORE</span>
  </div>

  <section class="abs register">
    <header>Registration Form</header>
    <p class="intro">Sign up to join the Onward Valley movement, and we will help you stay informed.</p>
    <span class="field">First name</span>
    <span class="field">Last name</span>
    <span class="field">Email id</span>
    <span class="signup">SIGNUP</span>
  </section>

  <h2 class="abs h2" style="left:586px;top:872px">Testimonials</h2>
  <div class="abs arrows">
    <svg width="17" height="17" viewBox="0 0 17 17"><circle cx="8.5" cy="8.5" r="8.5" fill="#aaa"/><path d="M10 5 6.5 8.5 10 12" stroke="#fff" stroke-width="2" fill="none"/></svg>
    <svg width="17" height="17" viewBox="0 0 17 17"><circle cx="8.5" cy="8.5" r="8.5" fill="#aaa"/><path d="M7 5 10.5 8.5 7 12" stroke="#fff" stroke-width="2" fill="none"/></svg>
  </div>
  <span class="abs qmark" style="left:590px;top:917px">&ldquo;</span>
  <p class="abs quote">Fusce feugiat malesuada odio. Morbi nunc dogravida at, cursus nec, luctus a, lorem. Maecnas tristique orca cd sem. Lorem ipsum dolorsit amet. Claritas est etiam processus dynamicus, qui sequitur mutationem consi uetudium lectorum. Mirum est notare quam littera go thica, quam nunc putamus parum claram</p>
  <span class="abs qmark" style="left:822px;top:1020px">&rdquo;</span>
  <div class="abs author">
    <svg width="12" height="11" viewBox="0 0 12 11"><circle cx="6" cy="3" r="3" fill="#444"/><path d="M0 11c0-4 3-5 6-5s6 1 6 5z" fill="#444"/></svg>
    Mira Holt's
  </div>

  <footer class="abs footer">
    <div class="links">About Us | Mission | Our Services | Shadow Support | For Referrers</div>
    <div class="copy">Copyright&nbsp; 2013.&nbsp; All rights reserved.</div>
    <div class="social">
      <i style="background:#3b5ab0"></i>
      <i style="background:#2ba3e0"></i>
      <i style="background:#f28a17"></i>
      <i style="background:#d9262a"></i>
    </div>
  </footer>
</div>
</body>
</html>
```